Jobinserat Vorlage medizinischer Bereich
Sehr gute Kommunikation auch mit Rückfragen damit das Projekt komplett verstanden wurde. Schnelle Umsetzung mit tollen Vorschlägen. Nur zu empfehlen!
Zielgruppe
Personalagentur im medizinischen Bereich (Krankenpfleger/Fachärzte)
Zielgruppe: Jobsuchende Krankenpflege Fachleute in Deutschland für die Schweiz!
Aufgabenstellung
jung, frisch, emotionell, verlockend
Bitte Text beachten: klinikpflegeleiterin
Wir benötigen ein Layout für ein Stelleninserat welches wir auf bei www.pflegestellenboerse.de platzieren möchten sowie auf www.medizinerkarriere.de / Das Format wird A4 sein, entweder eine oder zwei Seiten, je nachdem was für eine Stelle wir ausschreiben. Wichtig ist das Logo und der Text (siehe Projektanlage). Als Anhaltspunkt geht das Inserat (http://www.pflegestellenboerse.de/job/dipl-pflegefachfraudipl-pflegefachmann-hffh-oder-fage-fur-kurzeinsatze-10-20) in die Richtige Richtung, einfach mit unserer Farbe vom Logo oder der Academy http://www.valorintgruppe.com/academy/

```html
<!DOCTYPE html>
<html lang="de">
<head>
<meta charset="utf-8">
<title>Stelleninserat Klinikpflegeleitung</title>
<link rel="stylesheet" href="https://fonts.googleapis.com/css2?family=Source+Sans+3:wght@400;600;700&display=swap">
<style>
  :root{
    --orange:#eea41e;
    --dark:#454545;
    --text:#2b2b2b;
    --grey:#6d6d6d;
    --canvas:#f3f3f3;
    --paper:#ffffff;
  }
  *{box-sizing:border-box;margin:0;padding:0}
  html,body{width:1200px;height:1200px;overflow:hidden;background:var(--canvas)}
  body{font-family:"Source Sans 3",Arial,sans-serif;color:var(--text)}
  .sheet{
    position:absolute;left:0;top:0;width:597px;height:843px;
    background:var(--paper);
    transform-origin:0 0;
    transform:translate(196px,30px) scale(1.352);
    box-shadow:0 1px 4px rgba(0,0,0,.18);
  }
  .top-rule{position:absolute;left:0;top:0;width:100%;height:6px;background:var(--orange)}
  .hero{
    position:absolute;left:0;top:6px;width:100%;height:237px;
    background:
      radial-gradient(ellipse 22% 60% at 82% 70%, rgba(200,40,30,.85), rgba(200,40,30,0) 70%),
      radial-gradient(ellipse 18% 55% at 58% 62%, #f6f6f6, rgba(246,246,246,0) 75%),
      linear-gradient(90deg,#cfd6de 0%,#e8e2d6 35%,#ddd3c3 60%,#ece9e4 100%);
  }
  .eyebrow{
    position:absolute;left:0;top:220px;width:207px;height:42px;
    background:var(--orange);color:var(--dark);
    font-size:32.5px;font-weight:600;line-height:42px;padding-left:24px;
  }
  .title-band{
    position:absolute;left:0;top:266px;width:100%;height:42px;
    background:var(--dark);color:#fff;
    font-size:26.5px;font-weight:600;line-height:42px;text-align:left;padding-left:79px;white-space:nowrap;
  }
  .content{position:absolute;left:79px;top:325px;width:442px;font-size:10.6px;line-height:11.8px}
  .content h2{font-size:11.5px;font-weight:700;margin-bottom:6px}
  .list{list-style:none;margin-bottom:15px}
  .list li{position:relative;padding-left:13px;margin-bottom:3.2px}
  .list li::before{content:"";position:absolute;left:0;top:3.5px;width:5px;height:5px;background:var(--orange)}
  .list li.justified{text-align:justify;text-align-last:justify}
  .content p{margin-top:13px}
  .content p:first-of-type{margin-top:15px}
  .content strong{font-weight:700}
  .advisor{position:absolute;left:79px;top:729px;font-size:10.6px;line-height:12.3px}
  .advisor h3{font-size:10.6px;font-weight:700;margin-bottom:6px}
  .social{margin-top:12px;display:flex;align-items:center;gap:5px}
  .social-mark{width:11px;height:11px;background:#3b5a98}
  .brand{position:absolute;left:345px;top:752px;width:185px}
  .brand-name{font-size:21px;font-weight:400;color:var(--orange);line-height:24px;letter-spacing:.3px}
  .brand-address{margin-top:9px;font-size:6.4px;line-height:8px;color:var(--text)}
  .bottom-rule{position:absolute;left:0;bottom:0;width:100%;height:7px;background:var(--dark)}
</style>
</head>
<body>
  <main class="sheet">
    <div class="top-rule"></div>
    <div class="hero" role="img" aria-label="Foto: junger Arzt mit Brille, Kittel, Stethoskop und rotem Umhang in Heldenpose vor einem Büroregal"></div>
    <div class="eyebrow">Wir suchen</div>
    <h1 class="title-band">Klinikpflegeleiterin / Klinikpflegeleiter</h1>

    <section class="content">
      <h2>Ihre Aufgaben:</h2>
      <ul class="list">
        <li class="justified">Sicherstellung einer wirksamen, wirtschaftlichen und zweckmässigen Pflege und Betreuung</li>
        <li>Führung und Förderung der unterstellten Mitarbeitenden inklusive Stellenplanbewirtschaftung</li>
        <li>Mitwirkung bei der strategischen Weiterentwicklung von unternehmensweiten Projekten<br>und Kliniken</li>
        <li>Gewährleistung des Ausbildungsauftrages auf der Grund- und Tertiärstufe</li>
        <li>Qualitätssicherung und Prozessoptimierung gemäss der Unternehmensstrategie</li>
      </ul>

      <h2>Anfoderungen:</h2>
      <ul class="list">
        <li>Dipl. Pflegefachfrau/-mann HF, DN II, AKP, FH, DGKS</li>
        <li>Fundierte Führungserfahrung mit einer ausgewiesenen Managementweiterbildung auf<br>Fachhochschulniveau oder einer vergleichbaren Weiterbildung</li>
        <li>Hohe Patientenorientierung</li>
        <li>Konzeptionelle Fähigkeiten verbunden mit Innovationskraft und unternehmerischen Denken<br>und Handeln</li>
        <li>Kommunikative und teamorientierte Persönlichkeit mit betriebswirtschaftlichen und<br>organisatorischen Fähigkeiten</li>
        <li>Engagement für eine interdisziplinäre und interprofessionelle Zusammenarbeit mit einem<br>hohen Mass an Verantwortungsbereitschaft</li>
      </ul>

      <p>Suchen Sie eine verantwortungsvolle Herausforderung in einem familiären, dynamischen Umfeld<br>mit attraktiven Entwicklungsmöglichkeiten?</p>
      <p><strong>Wir garantieren Ihnen absolute Diskretion.</strong></p>
      <p>Für einen ersten vertraulichen Kontakt steht Ihnen Herr <strong>Lukas Brenner</strong> gerne zur Verfügung.<br>
      Zögern Sie nicht, wir freuen uns auf Ihre komplette online Bewerbung mit Foto per E-Mail an:<br>
      <strong>lukas.brenner@valorintgruppe.com</strong></p>
    </section>

    <section class="advisor">
      <h3>Ihr Berater:</h3>
      <div>Lukas Brenner</div>
      <div>Tel. +41 44 000 12 34</div>
      <div>Mail: lukas.brenner@valorintgruppe.com</div>
      <div>Web: valorintgruppe.com</div>
      <div class="social">Finde uns auf <span class="social-mark"></span></div>
    </section>

    <section class="brand">
      <div class="brand-name">Valorint<br>Recruitment Group</div>
      <div class="brand-address">Valorint – Recruitment Group Ltd.<br>Lindenweg 7 | CH-9999 Musterdorf</div>
    </section>

    <div class="bottom-rule"></div>
  </main>
</body>
</html>
```